SEO wiki for a know-how website (rankvale.ch)

Hi,

i need a know-how wiki for an SEO website that looks similar to:

http://demo.plumtorx.com/#knowhow

With following know-how categories instead of "account settings" and "API questions":
- Content SEO
- Technical SEO
- Link building
- Influencer marketing
- paid marketing
- analytics & measurement

So i Need the following pages:
1. Landing page with the categories, the search bar and the side-bar
- Sidebar has latest articles, popular articles and categories (in this order)
- On top a nice logo
- on top right -> blog, contact
- on top right below -> social media buttons: corvaline, chirpnest

2. a blog site with
- headline
- sub-headline
- date, name
- rating with 5 "know-how" stars
- picture
- article
- info about the author
- related articles
- integration of comment plugin VORBLE

Target Market(s)

SEO folks

Industry/Entity Type

Seo

Logo Text

Own-hands tuning SEO

Number of Pages Required

2 page

Font styles to use
Sans Serif

Colors

Designer to choose colors to be used in the design.

```html
<!DOCTYPE html>
<html lang="en">
<head>
<meta charset="utf-8">
<title>RANKVALE Know-how</title>
<link rel="stylesheet" href="https://fonts.googleapis.com/css2?family=Poppins:wght@400;500;600;700&family=Open+Sans:wght@400;600&display=swap">
<style>
  :root{
    --blue:#2f5b9e;
    --blue-line:#3d6aad;
    --orange:#f57c12;
    --text:#555a60;
    --heading:#333;
    --divider:#e3e3e3;
    --footer-bg:#efefef;
    --white:#fff;
  }
  *{margin:0;padding:0;box-sizing:border-box}
  html,body{width:971px;height:1200px;overflow:hidden;background:var(--white)}
  body{position:relative;font-family:'Poppins',sans-serif;color:var(--text)}
  ul{list-style:none}
  a{color:inherit;text-decoration:none}

  .site-header{position:absolute;left:0;top:0;width:971px;height:71px}
  .brand{position:absolute;left:80px;top:17px;font-family:'Poppins',sans-serif;font-weight:700;font-size:29px;letter-spacing:0.5px;color:var(--blue);line-height:36px}
  .main-nav{position:absolute;right:80px;top:25px;display:flex;align-items:center;gap:16px;font-family:'Open Sans',sans-serif;font-size:11.5px;color:#333}
  .social{display:flex;gap:8px;margin-left:6px}
  .social a{font-family:'Open Sans',sans-serif;font-weight:600;font-size:10.5px;color:var(--blue)}

  .hero{position:absolute;left:0;top:71px;width:971px;height:159px;background:linear-gradient(180deg,#5b83bd 0%,#4a74b1 55%,#3f69a6 80%,#5a7fb6 100%)}
  .search{position:absolute;left:254px;top:61px;width:462px;height:36px;background:var(--white);border-radius:18px;display:flex;align-items:center;padding:0 7px 0 18px}
  .search-input{flex:1;font-family:'Open Sans',sans-serif;font-size:9.5px;color:#555}
  .search-btn{width:72px;height:24px;border-radius:12px;background:var(--orange);color:var(--white);font-family:'Open Sans',sans-serif;font-size:11px;font-weight:600;display:flex;align-items:center;justify-content:center}

  .title-bar{position:absolute;height:33px;border-bottom:1px solid var(--blue-line)}
  .title-bar span{display:block;height:33px;background:var(--blue);color:var(--white);font-weight:600;font-size:15.5px;line-height:34px;padding-left:11px;letter-spacing:0.2px;white-space:nowrap}

  .doc-ico{width:9px;height:10px;flex:none}
  .link-list li{display:flex;align-items:center;gap:7px;height:23.6px;font-size:11px;color:var(--text);white-space:nowrap}

  .cat{position:absolute;width:260px}
  .cat-head{display:flex;align-items:center;gap:11px;height:32px}
  .cat-icon{width:32px;height:32px;border-radius:50%;display:flex;align-items:center;justify-content:center;flex:none}
  .cat-icon.blue{background:var(--blue)}
  .cat-icon.orange{background:var(--orange)}
  .cat-head h2{font-weight:400;font-size:15.5px;color:var(--heading);letter-spacing:0.3px;white-space:nowrap}
  .cat .link-list{margin-top:12px}

  .grid-line-v{position:absolute;left:342px;top:361px;width:1px;height:690px;background:var(--divider)}
  .grid-line-h{position:absolute;left:80px;width:565px;height:1px;background:var(--divider)}

  .side-list{position:absolute;left:679px;width:270px}
  .side-list.cats li{gap:8px}
  .bullet{width:9px;height:9px;flex:none}

  .site-footer{position:absolute;left:0;top:1102px;width:971px;height:98px;background:var(--footer-bg);font-family:'Open Sans',sans-serif;font-size:9.5px;color:#333}
  .footer-nav{position:absolute;top:33px;left:0;width:944px;display:flex;justify-content:center;gap:10px}
  .copyright{position:absolute;top:56px;left:0;width:944px;text-align:center}
</style>
</head>
<body>

<header class="site-header">
  <div class="brand">RANKVALE</div>
  <nav class="main-nav">
    <a href="#">Blog</a>
    <a href="#">Contact</a>
    <div class="social">
      <a href="#">Corvaline</a>
      <a href="#">Chirpnest</a>
    </div>
  </nav>
</header>

<section class="hero" role="img" aria-label="City skyline photo in blue tones behind the search bar">
  <div class="search">
    <span class="search-input">Have a question? Ask or enter a search term.</span>
    <span class="search-btn">SEARCH</span>
  </div>
</section>

<svg width="0" height="0" style="position:absolute">
  <defs>
    <symbol id="doc" viewBox="0 0 9 10"><path d="M1 .5h4.5L8 3v6.5H1z" fill="none" stroke="#777" stroke-width="0.9"/><path d="M2.6 4.6h3.8M2.6 6.2h3.8M2.6 7.8h3.8" stroke="#777" stroke-width="0.8"/></symbol>
    <symbol id="circ" viewBox="0 0 9 9"><circle cx="4.5" cy="4.5" r="4.5" fill="#666"/><path d="M3.6 2.6l2 1.9-2 1.9" fill="none" stroke="#fff" stroke-width="1.2"/></symbol>
  </defs>
</svg>

<main>
  <div class="title-bar" style="left:80px;top:288px;width:563px">
    <span style="width:213px;clip-path:polygon(0 0,178px 0,100% 100%,0 100%)">ARTICLE CATEGORIES</span>
  </div>

  <div class="grid-line-v"></div>
  <div class="grid-line-h" style="top:578px"></div>
  <div class="grid-line-h" style="top:821px"></div>

  <article class="cat" style="left:79px;top:363px">
    <div class="cat-head"><span class="cat-icon blue"><svg width="13" height="14" viewBox="0 0 9 10"><path d="M1 .5h4.5L8 3v6.5H1z" fill="none" stroke="#fff" stroke-width="0.9"/><path d="M2.6 4.6h3.8M2.6 6.2h3.8M2.6 7.8h3.8" stroke="#fff" stroke-width="0.8"/></svg></span><h2>CONTENT SEO</h2></div>
    <ul class="link-list">
      <li><svg class="doc-ico"><use href="#doc"/></svg>Duis aute irure dolor in reprehenderit</li>
      <li><svg class="doc-ico"><use href="#doc"/></svg>Excepteur sint occaecat cupidatat non</li>
      <li><svg class="doc-ico"><use href="#doc"/></svg>Nemo enim ipsam voluptatem quia</li>
      <li><svg class="doc-ico"><use href="#doc"/></svg>Ut enim ad minima veniam, quis nostrum</li>
      <li><svg class="doc-ico"><use href="#doc"/></svg>Quis autem vel eum iure reprehenderit</li>
      <li><svg class="doc-ico"><use href="#doc"/></svg>Nor again is there anyone who</li>
    </ul>
  </article>

  <article class="cat" style="left:388px;top:363px">
    <div class="cat-head"><span class="cat-icon orange"><svg width="14" height="14" viewBox="0 0 14 14"><circle cx="5" cy="8" r="3" fill="none" stroke="#fff" stroke-width="1.8"/><circle cx="10" cy="4" r="2" fill="none" stroke="#fff" stroke-width="1.5"/></svg></span><h2>TECHNICAL SEO</h2></div>
    <ul class="link-list">
      <li><svg class="doc-ico"><use href="#doc"/></svg>Duis aute irure dolor in reprehenderit</li>
      <li><svg class="doc-ico"><use href="#doc"/></svg>Excepteur sint occaecat cupidatat non</li>
      <li><svg class="doc-ico"><use href="#doc"/></svg>Nemo enim ipsam voluptatem quia</li>
      <li><svg class="doc-ico"><use href="#doc"/></svg>Ut enim ad minima veniam, quis nostrum</li>
      <li><svg class="doc-ico"><use href="#doc"/></svg>Quis autem vel eum iure reprehenderit</li>
      <li><svg class="doc-ico"><use href="#doc"/></svg>Nor again is there anyone who</li>
    </ul>
  </article>

  <article class="cat" style="left:79px;top:611px">
    <div class="cat-head"><span class="cat-icon orange"><svg width="14" height="14" viewBox="0 0 14 14"><rect x="1.5" y="5.5" width="6" height="4" rx="2" transform="rotate(-45 4.5 7.5)" fill="none" stroke="#fff" stroke-width="1.5"/><rect x="6.5" y="4.5" width="6" height="4" rx="2" transform="rotate(-45 9.5 6.5)" fill="none" stroke="#fff" stroke-width="1.5"/></svg></span><h2>LINK BUILDING</h2></div>
    <ul class="link-list">
      <li><svg class="doc-ico"><use href="#doc"/></svg>Duis aute irure dolor in reprehenderit</li>
      <li><svg class="doc-ico"><use href="#doc"/></svg>Excepteur sint occaecat cupidatat non</li>
      <li><svg class="doc-ico"><use href="#doc"/></svg>Nemo enim ipsam voluptatem quia</li>
      <li><svg class="doc-ico"><use href="#doc"/></svg>Ut enim ad minima veniam, quis nostrum</li>
      <li><svg class="doc-ico"><use href="#doc"/></svg>Quis autem vel eum iure reprehenderit</li>
      <li><svg class="doc-ico"><use href="#doc"/></svg>Nor again is there anyone who</li>
    </ul>
  </article>

  <article class="cat" style="left:388px;top:611px">
    <div class="cat-head"><span class="cat-icon blue"><svg width="15" height="13" viewBox="0 0 15 13"><path d="M1 1v11h13" fill="none" stroke="#fff" stroke-width="1.5"/><path d="M3.5 9l3-3.5 2.5 2L13 3" fill="none" stroke="#fff" stroke-width="1.6"/></svg></span><h2>INFLUENCER MARKETING</h2></div>
    <ul class="link-list">
      <li><svg class="doc-ico"><use href="#doc"/></svg>Duis aute irure dolor in reprehenderit</li>
      <li><svg class="doc-ico"><use href="#doc"/></svg>Excepteur sint occaecat cupidatat non</li>
      <li><svg class="doc-ico"><use href="#doc"/></svg>Nemo enim ipsam voluptatem quia</li>
      <li><svg class="doc-ico"><use href="#doc"/></svg>Ut enim ad minima veniam, quis nostrum</li>
      <li><svg class="doc-ico"><use href="#doc"/></svg>Quis autem vel eum iure reprehenderit</li>
      <li><svg class="doc-ico"><use href="#doc"/></svg>Nor again is there anyone who</li>
    </ul>
  </article>

  <article class="cat" style="left:79px;top:854px">
    <div class="cat-head"><span class="cat-icon blue"><svg width="15" height="14" viewBox="0 0 15 14"><path d="M1 2v5l6 6 6-6-6-6H2z" fill="#fff"/><circle cx="4" cy="4.5" r="1.2" fill="#2f5b9e"/></svg></span><h2>PAID MARKETING</h2></div>
    <ul class="link-list">
      <li><svg class="doc-ico"><use href="#doc"/></svg>Duis aute irure dolor in reprehenderit</li>
      <li><svg class="doc-ico"><use href="#doc"/></svg>Excepteur sint occaecat cupidatat non</li>
      <li><svg class="doc-ico"><use href="#doc"/></svg>Nemo enim ipsam voluptatem quia</li>
      <li><svg class="doc-ico"><use href="#doc"/></svg>Ut enim ad minima veniam, quis nostrum</li>
      <li><svg class="doc-ico"><use href="#doc"/></svg>Quis autem vel eum iure reprehenderit</li>
      <li><svg class="doc-ico"><use href="#doc"/></svg>Nor again is there anyone who</li>
    </ul>
  </article>

  <article class="cat" style="left:388px;top:854px">
    <div class="cat-head"><span class="cat-icon orange"><svg width="13" height="13" viewBox="0 0 13 13"><circle cx="5.5" cy="5.5" r="3.8" fill="none" stroke="#fff" stroke-width="1.8"/><path d="M8.3 8.3L12 12" stroke="#fff" stroke-width="2"/></svg></span><h2>ANALYTICS &amp; MEASUREMENT</h2></div>
    <ul class="link-list">
      <li><svg class="doc-ico"><use href="#doc"/></svg>Duis aute irure dolor in reprehenderit</li>
      <li><svg class="doc-ico"><use href="#doc"/></svg>Excepteur sint occaecat cupidatat non</li>
      <li><svg class="doc-ico"><use href="#doc"/></svg>Nemo enim ipsam voluptatem quia</li>
      <li><svg class="doc-ico"><use href="#doc"/></svg>Ut enim ad minima veniam, quis nostrum</li>
      <li><svg class="doc-ico"><use href="#doc"/></svg>Quis autem vel eum iure reprehenderit</li>
      <li><svg class="doc-ico"><use href="#doc"/></svg>Nor again is there anyone who</li>
    </ul>
  </article>
</main>

<aside>
  <div class="title-bar" style="left:680px;top:288px;width:212px">
    <span style="width:178px;clip-path:polygon(0 0,144px 0,100% 100%,0 100%)">LATEST ARTICLES</span>
  </div>
  <ul class="link-list side-list" style="top:337px">
    <li><svg class="doc-ico"><use href="#doc"/></svg>Duis aute irure dolor in reprehenderit</li>
    <li><svg class="doc-ico"><use href="#doc"/></svg>Excepteur sint occaecat cupidatat non</li>
    <li><svg class="doc-ico"><use href="#doc"/></svg>Nemo enim ipsam voluptatem quia</li>
    <li><svg class="doc-ico"><use href="#doc"/></svg>Ut enim ad minima veniam, quis nostrum</li>
    <li><svg class="doc-ico"><use href="#doc"/></svg>Quis autem vel eum iure reprehenderit</li>
    <li><svg class="doc-ico"><use href="#doc"/></svg>Nor again is there anyone who</li>
  </ul>

  <div class="title-bar" style="left:680px;top:517px;width:212px">
    <span style="width:185px;clip-path:polygon(0 0,151px 0,100% 100%,0 100%)">POPULAR ARTICLES</span>
  </div>
  <ul class="link-list side-list" style="top:566px">
    <li><svg class="doc-ico"><use href="#doc"/></svg>How Secure Is My Password?</li>
    <li><svg class="doc-ico"><use href="#doc"/></svg>What Technologies Are Used?</li>
    <li><svg class="doc-ico"><use href="#doc"/></svg>How Do I Change My Password?</li>
    <li><svg class="doc-ico"><use href="#doc"/></svg>Can I Change My Username?</li>
    <li><svg class="doc-ico"><use href="#doc"/></svg>Excepteur sint occaecat cupidatat non</li>
    <li><svg class="doc-ico"><use href="#doc"/></svg>Nemo enim ipsam voluptatem quia</li>
  </ul>

  <div class="title-bar" style="left:680px;top:739px;width:212px">
    <span style="width:185px;clip-path:polygon(0 0,151px 0,100% 100%,0 100%)">CATEGORIES</span>
  </div>
  <ul class="link-list side-list cats" style="top:788px">
    <li><svg class="bullet"><use href="#circ"/></svg>Account Settings 6</li>
    <li><svg class="bullet"><use href="#circ"/></svg>API Questions 5</li>
    <li><svg class="bullet"><use href="#circ"/></svg>Billing 6</li>
    <li><svg class="bullet"><use href="#circ"/></svg>Copyright &amp; Legal 5</li>
    <li><svg class="bullet"><use href="#circ"/></svg>Customization 3</li>
    <li><svg class="bullet"><use href="#circ"/></svg>Mobile Apps 5</li>
    <li><svg class="bullet"><use href="#circ"/></svg>Upgrading 2</li>
    <li><svg class="bullet"><use href="#circ"/></svg>Using Wikidesk</li>
  </ul>
</aside>

<footer class="site-footer">
  <nav class="footer-nav">
    <a href="#">Home</a><span>/</span>
    <a href="#">About Us</a><span>/</span>
    <a href="#">Privacy Policy</a><span>/</span>
    <a href="#">Contact Us</a>
  </nav>
  <p class="copyright">2017 © Copyrights RANKVALE.All Rights Reserved</p>
</footer>

</body>
</html>
```